Capability Statement Brochure - Corporate

We need to provide our corporate clients with an elegant, professional and well designed capability statement that not only details what our business can offer, but reflects our professionalism with relevant technical photos. I am thinking two pages A 4 pdf will be suitable if the text can fit without looking crowded but happy to extend to 3 or 4 pages if needed . Colours and details can be taken from our website www.quorintech.com.au Some photos have been attached however if we need more professional stock photos I am happy to use them if needed. This project needs to convince potential clients we are the best in industry and our capability is extensive. Please help us relay this to our customers. Thank you,.

Target Market(s)

Corporate, Government, Education, Defence, Healthcare

Industry/Entity Type

Audio Visual Integration

Colors
0054AA
0677BA
7BADD7
CADEEF
E8F1F8

Requirements
Must have
• Style, look classy, sophisticated and technical
Nice to have
• Quorin Tech colours, Logo, website and email and include the PRISM LED Logo
Should not have
• Messy, too much clutter, not easy to read.

```html
<!DOCTYPE html>
<html lang="en">
<head>
<meta charset="utf-8">
<title>Quorin Tech Capability Statement</title>
<link href="https://fonts.googleapis.com/css2?family=Montserrat:wght@500;700;800&family=Open+Sans:wght@400;600&display=swap" rel="stylesheet">
<style>
:root{
  --navy:#0b2b5e;
  --blue:#0054AA;
  --mid:#0677BA;
  --sky:#7BADD7;
  --pale:#CADEEF;
  --mist:#E8F1F8;
  --orange:#f27a1f;
  --ink:#4a5563;
  --bg:#eceef1;
  --white:#ffffff;
}
*{box-sizing:border-box;margin:0;padding:0}
html,body{width:861px;height:1200px;overflow:hidden;background:var(--bg)}
body{position:relative;font-family:"Open Sans",sans-serif;color:var(--ink)}
.page{position:absolute;width:340px;height:480px;background:var(--white);box-shadow:0 4px 14px rgba(0,0,0,.18);overflow:hidden}
.p1{left:75px;top:60px}.p2{left:446px;top:60px}.p3{left:75px;top:600px}.p4{left:446px;top:600px}
.abs{position:absolute}
.brand{font-family:"Montserrat",sans-serif;font-weight:700;color:var(--blue);display:flex;align-items:center;gap:4px}
.brand .mark{width:9px;height:9px;background:var(--blue)}
.photo{position:absolute}
.h{font-family:"Montserrat",sans-serif;font-weight:700}
.para{font-size:4.2px;line-height:1.5;color:var(--ink)}
.footer{position:absolute;left:0;right:0;bottom:0;height:16px;border-top:1px solid var(--pale);font-size:4.5px;display:flex;align-items:center;justify-content:space-between;padding:0 16px;color:var(--ink)}
.footer .bar{width:60px;height:3px;background:var(--blue)}
.badge{position:absolute;background:var(--navy);color:var(--white);font-family:"Montserrat",sans-serif;font-weight:700;display:flex;align-items:center;justify-content:center}
.list{list-style:none;font-size:4.4px;line-height:1.9}
.list li{display:flex;align-items:center;gap:3px}
.tick{width:5px;height:5px;border-radius:50%;background:var(--orange);flex:none}
.icon{width:12px;height:12px;border-radius:50%;background:var(--orange);flex:none}
.sector{position:absolute;left:16px;width:150px}
.sector .h{font-size:5.5px;color:var(--navy);display:flex;align-items:center;gap:5px;margin-bottom:3px}
.cover-title{z-index:2}
</style>
</head>
<body>

<section class="page p1">
  <div class="brand abs" style="left:110px;top:30px;font-size:13px"><span class="mark"></span>Quorin Tech</div>
  <div class="abs" style="left:128px;top:48px;font-size:4px;letter-spacing:.4px;color:var(--mid)">AUDIO VISUAL INTEGRATION SPECIALISTS</div>
  <svg class="abs" style="left:0;top:70px" width="340" height="230" viewBox="0 0 340 230">
    <polygon points="0,20 60,0 60,200 0,215" fill="var(--blue)"/>
    <polygon points="0,165 80,150 80,205 0,228" fill="var(--navy)"/>
    <polygon points="300,20 340,10 340,200 300,212" fill="var(--mid)"/>
  </svg>
  <div class="photo" role="img" aria-label="Boardroom with conference table, chairs and wall display" style="left:40px;top:80px;width:270px;height:190px;background:linear-gradient(160deg,#dfe3e8,#b8c0c9 60%,#7d858f)"></div>
  <div class="h abs cover-title" style="left:28px;top:318px;font-size:23px;line-height:1.05;color:var(--navy);font-weight:800">CAPABILITY<br>STATEMENT</div>
  <div class="abs" style="left:28px;top:372px;width:120px;height:3px;background:var(--orange)"></div>
  <div class="badge" style="left:215px;top:325px;width:95px;height:34px;font-size:11px;background:var(--navy)">PRISM LED</div>
  <div class="abs" style="left:28px;top:395px;font-size:6px;color:var(--blue);font-weight:600">www.quorintech.com.au</div>
  <div class="abs" style="left:0;bottom:0;width:340px;height:14px;background:var(--blue)"></div>
</section>

<section class="page p2">
  <div class="h abs" style="left:16px;top:20px;font-size:12px;color:var(--blue)">Company Overview</div>
  <svg class="abs" style="right:16px;top:16px" width="26" height="16"><polygon points="0,16 12,0 26,0 14,16" fill="var(--blue)"/></svg>
  <p class="para abs" style="left:16px;top:40px;width:308px">Quorin Tech is an audio visual integrator delivering considered, reliable solutions to corporate, government, education, defence and healthcare clients. Our team designs, installs and supports systems that help people meet, learn and share with ease.</p>
  <p class="para abs" style="left:16px;top:64px;width:308px">From single rooms to whole campuses, we manage each stage with care, clear documentation and certified engineers, so every project is delivered on time and ready for daily use.</p>
  <div class="abs" style="left:16px;top:100px;display:flex;flex-direction:column;gap:4px">
    <div class="icon" style="width:22px;height:22px"></div>
    <div class="h" style="font-size:10px;line-height:1.05;color:var(--orange)">Core<br>Capabilities</div>
  </div>
  <ul class="list abs" style="left:130px;top:98px;color:var(--navy)">
    <li><span class="tick"></span>AV System Design and Engineering</li>
    <li><span class="tick"></span>Video Conferencing and Unified Comms</li>
    <li><span class="tick"></span>LED Video Walls and Digital Signage</li>
    <li><span class="tick"></span>Control Systems and Automation</li>
    <li><span class="tick"></span>Audio Reinforcement and DSP</li>
    <li><span class="tick"></span>Installation and Commissioning</li>
    <li><span class="tick"></span>Service, Support and Maintenance</li>
    <li><span class="tick"></span>Project Management and Training</li>
  </ul>
  <div class="sector" style="top:210px;width:170px">
    <div class="h"><span class="icon"></span>LED Video Wall Expertise</div>
    <p class="para">We design and install fine pitch LED walls for lobbies, control rooms and boardrooms, matched to each space for clear, bright and even images from every seat.</p>
  </div>
  <div class="photo" role="img" aria-label="LED video wall installation" style="left:16px;top:275px;width:160px;height:170px;background:linear-gradient(135deg,#2a3d5a,#6f8db0)"></div>
  <div class="abs" style="left:190px;top:210px;width:134px;height:235px;background:var(--blue);padding:12px 10px;color:var(--white)">
    <div class="h" style="font-size:8px;margin-bottom:8px">Markets Served</div>
    <ul class="list" style="color:var(--white)">
      <li><span class="tick"></span>Corporate</li>
      <li><span class="tick"></span>Government</li>
      <li><span class="tick"></span>Education</li>
      <li><span class="tick"></span>Defence</li>
      <li><span class="tick"></span>Healthcare</li>
      <li><span class="tick"></span>Mining and Resources</li>
    </ul>
  </div>
  <div class="footer"><span>www.quorintech.com.au</span><span class="bar"></span></div>
</section>

<section class="page p3">
  <div class="sector" style="top:22px"><div class="h"><span class="icon"></span>Healthcare Experience</div><p class="para">Clinical training rooms, theatres and boardrooms built to strict hospital standards and workflows.</p></div>
  <div class="sector" style="top:90px"><div class="h"><span class="icon"></span>Corporate Enterprise</div><p class="para">Meeting spaces, town halls and offices with simple, consistent control across every site.</p></div>
  <div class="sector" style="top:158px"><div class="h"><span class="icon"></span>Government &amp; Defence</div><p class="para">Secure conferencing and briefing rooms delivered by cleared staff to the required standards.</p></div>
  <div class="sector" style="top:226px"><div class="h"><span class="icon"></span>Mining &amp; Resources</div><p class="para">Remote operations centres and site rooms built for durability and round the clock use.</p></div>
  <div class="sector" style="top:294px"><div class="h"><span class="icon"></span>Education</div><p class="para">Lecture theatres, hybrid classrooms and campus signage that staff and students use with ease.</p></div>
  <div class="photo" role="img" aria-label="Hospital operating theatre with medical displays" style="left:180px;top:0;width:160px;height:165px;background:linear-gradient(160deg,#e9eef3,#a9b8c6)"></div>
  <div class="h abs" style="left:190px;top:175px;font-size:9px;line-height:1.15;color:var(--orange)">DESIGN &amp;<br>ENGINEERING</div>
  <div class="abs" style="left:180px;top:205px;width:144px;height:190px;background:var(--blue);padding:12px 10px">
    <p class="para" style="color:var(--white)">Our engineers create detailed designs, schematics and rack layouts for every project. Each system is planned around how people use the room, with room for growth and simple upkeep.</p>
    <p class="para" style="color:var(--white);margin-top:6px">Designs are reviewed with clients at each stage to keep scope, budget and timing clear.</p>
  </div>
  <div class="footer"><span>www.quorintech.com.au</span><span class="bar"></span></div>
</section>

<section class="page p4">
  <div class="photo" role="img" aria-label="Auditorium with seating and large projection screen" style="left:0;top:0;width:340px;height:150px;background:linear-gradient(160deg,#3c4a5e,#8a6f5a 70%,#b48a66)"></div>
  <div class="abs" style="left:0;top:0;width:120px;height:150px;background:rgba(11,43,94,.8);padding:16px 12px">
    <div class="icon" style="margin-bottom:6px"></div>
    <div class="h" style="font-size:8px;color:var(--white);line-height:1.2">Implementation &amp;<br>Commissioning</div>
    <p class="para" style="color:var(--white);margin-top:6px">Installed by our own teams and tested in full before handover.</p>
  </div>
  <div class="sector" style="top:165px;width:80px"><div class="h"><span class="icon"></span>Service &amp; Support</div><p class="para">Help desk, remote monitoring and fast on site response.</p></div>
  <div class="sector" style="top:165px;left:105px;width:85px"><div class="h"><span class="icon"></span>Maintenance &amp; Upgrades</div><p class="para">Planned checks and upgrades keep systems current.</p></div>
  <div class="photo" role="img" aria-label="Technician working at equipment rack" style="left:16px;top:230px;width:170px;height:120px;background:linear-gradient(135deg,#5d6e85,#aab6c4)"></div>
  <div class="abs" style="left:200px;top:160px;width:124px;height:190px;background:var(--orange);padding:12px 10px;color:var(--white)">
    <div class="h" style="font-size:7.5px;line-height:1.2;margin-bottom:8px">Why Choose Quorin Tech Systems</div>
    <ul class="list" style="color:var(--white)">
      <li><span class="tick" style="background:var(--white)"></span>Certified engineers</li>
      <li><span class="tick" style="background:var(--white)"></span>End to end delivery</li>
      <li><span class="tick" style="background:var(--white)"></span>Proven track record</li>
      <li><span class="tick" style="background:var(--white)"></span>Local support team</li>
      <li><span class="tick" style="background:var(--white)"></span>Vendor neutral advice</li>
    </ul>
  </div>
  <div class="abs" style="left:0;top:370px;width:340px;height:70px;background:var(--blue);display:flex;align-items:center;gap:8px;padding:0 16px;color:var(--white);font-size:4.4px;line-height:1.6">
    <div style="flex:1"><div class="h" style="font-size:5.5px">Phone</div>02 5550 1420</div>
    <div style="flex:1"><div class="h" style="font-size:5.5px">Email</div>info@quorintech.com.au</div>
    <div style="flex:1"><div class="h" style="font-size:5.5px">Web</div>www.quorintech.com.au</div>
    <div style="flex:1"><div class="h" style="font-size:5.5px">Office</div>12 Harbour Lane, Sydney</div>
    <div class="badge" style="position:static;width:54px;height:22px;font-size:6px;background:var(--navy)">PRISM LED</div>
  </div>
  <div class="footer"><span class="brand" style="font-size:6px"><span class="mark" style="width:6px;height:6px"></span>Quorin Tech</span><span class="bar"></span></div>
</section>

</body>
</html>
```